Banner for promote service of debit card

We are PagaVelo and we need the banners to be posted on the facebook and instagram pages.
We want something to communicate that it is an exclusive debit card full of services.
Low commissions.
Our competitors:
https://www.nortapay-pagos.it/it/home.html
https://www.zelkor-conti.it/it/
https://www.fotoreelz.it/serravanbank/
sendquillo
maybe some banner that makes the idea of a convenient debit card that everyone can use.
Girls enjoying card shopping.
Please check also website for slogans and phrases to use
https://www.pagavelo-carta.it/
Should show the services.
We must convey that it is a fast, simple card that guarantees privacy.
We need strong banners that attract people as these ban will be sponsored on instagram and facebook
Target Market(s)
People 18-35 y
Open Bank account. low commissions. Easy to use. No limits. 100% Privacy.
Requirements
Must have
- Written in Italian.

```html
<!DOCTYPE html>
<html lang="it">
<head>
<meta charset="utf-8">
<title>PagaVelo – Banner carta di debito</title>
<link rel="stylesheet" href="https://fonts.googleapis.com/css2?family=Barlow:wght@300;700&family=Montserrat:wght@600&display=swap">
<style>
  :root {
    --stage: #b3b3b3;
    --magenta: #c8106e;
    --coral: #f26b4f;
    --logo-grey: #808080;
    --teal: #4bbcc8;
    --teal-deep: #3fb3c2;
    --lilac: #a884d2;
    --lilac-deep: #9f78cc;
    --white: #ffffff;
  }
  * { margin: 0; padding: 0; box-sizing: border-box; }
  html, body { width: 1200px; height: 1200px; overflow: hidden; background: var(--stage); }
  .stage { position: relative; width: 1200px; height: 1200px; }

  .banner {
    position: absolute;
    width: 1108px;
    height: 469px;
    overflow: hidden;
    background: var(--white);
  }
  .banner--teal { left: 48px; top: 93px; }
  .banner--lilac { left: 46px; top: 611px; }

  .banner__bg { position: absolute; inset: 0; }
  .banner--teal .banner__bg {
    background: linear-gradient(212deg, var(--teal-deep) 0%, var(--teal) 25%, rgba(75,188,200,0.4) 50%, rgba(255,255,255,0.9) 66%, var(--white) 78%);
  }
  .banner--lilac .banner__bg {
    background: linear-gradient(212deg, var(--lilac-deep) 0%, var(--lilac) 25%, rgba(168,132,210,0.4) 50%, rgba(255,255,255,0.9) 66%, var(--white) 78%);
  }

  .banner__copy {
    position: absolute;
    left: 76px;
    top: 78px;
    font-family: "Barlow", Arial, sans-serif;
  }
  .banner__headline {
    font-weight: 700;
    font-size: 77px;
    line-height: 68px;
    letter-spacing: -0.3px;
    color: var(--magenta);
  }
  .banner__subline {
    margin-top: 16px;
    font-weight: 300;
    font-size: 42px;
    line-height: 48px;
    letter-spacing: 0.6px;
    color: var(--coral);
  }

  .brand {
    position: absolute;
    left: 231px;
    top: 306px;
    width: 200px;
    display: flex;
    flex-direction: column;
    align-items: center;
    gap: 12px;
  }
  .brand__dot {
    width: 56px; height: 56px;
    border-radius: 50%;
    background: var(--coral);
  }
  .brand__name {
    font-family: "Montserrat", Arial, sans-serif;
    font-weight: 600;
    font-size: 32px;
    line-height: 36px;
    color: var(--logo-grey);
  }

  .banner__photo { position: absolute; bottom: 0; }
  .banner--teal .banner__photo {
    left: 700px; width: 408px; top: 20px;
    border-radius: 160px 160px 0 0;
    background: linear-gradient(180deg, #c9a28c 0%, #3a2a25 35%, #1c1f26 55%, #141519 100%);
  }
  .banner--lilac .banner__photo {
    left: 680px; width: 390px; top: 20px;
    border-radius: 160px 160px 0 0;
    background: linear-gradient(180deg, #b86a3c 0%, #e2b69c 30%, #8e8c8a 55%, #7d7b79 100%);
  }
</style>
</head>
<body>
<main class="stage">

  <section class="banner banner--teal">
    <div class="banner__bg"></div>
    <div class="banner__copy">
      <h1 class="banner__headline">Troviamo la carta<br>più adatta a te.</h1>
      <p class="banner__subline">La carta più veloce di sempre.</p>
    </div>
    <div class="brand">
      <span class="brand__dot"></span>
      <span class="brand__name">PagaVelo</span>
    </div>
    <div class="banner__photo" role="img" aria-label="Foto di una giovane donna sorridente in giacca scura che mostra una carta di debito"></div>
  </section>

  <section class="banner banner--lilac">
    <div class="banner__bg"></div>
    <div class="banner__copy">
      <h2 class="banner__headline">Troviamo la carta<br>più adatta a te.</h2>
      <p class="banner__subline">La carta più veloce di sempre.</p>
    </div>
    <div class="brand">
      <span class="brand__dot"></span>
      <span class="brand__name">PagaVelo</span>
    </div>
    <div class="banner__photo" role="img" aria-label="Foto di un giovane uomo sorridente in maglione grigio che indica una carta di debito"></div>
  </section>

</main>
</body>
</html>
```